Crossword App Main Page Design

For a crossword application we need a main page. I am enclosing the current temporary design. There will be 5 buttons. We want a simple but attractive design. Vector designs are preferred. Thank you very much for your interest.
The name of the application is Polyglyph Gridword Riddle and the motto is "gridplay rebuilt." So please use this name on the screen.
Thwe designs I have received so far almost the same with one I have attached. Only the button colors and background image are different. Please try different placement and buttons.
Thanks

```html
<!DOCTYPE html>
<html lang="en">
<head>
<meta charset="utf-8">
<title>Polyglyph Gridword Riddle – Main Screen</title>
<link href="https://fonts.googleapis.com/css2?family=Arimo:wght@400;700&family=Comfortaa:wght@700&display=swap" rel="stylesheet">
<style>
  :root {
    --stage: #eef1f4;
    --sky-top: #4fb6ec;
    --sky-mid: #2f97dc;
    --sky-low: #1f7dc8;
    --band: #175fa3;
    --band-edge: #3b92d6;
    --status-top: #f4f5f6;
    --status-low: #c9cdd2;
    --status-ink: #1c1c1c;
    --signal: #2b6fd8;
    --battery: #4cc63c;
    --title: #ffffff;
    --gold-top: #ffd45a;
    --gold-low: #f29a12;
    --gold-ink: #0f3566;
    --tile-top: #1b5fa8;
    --tile-low: #0c3f7a;
    --ring: #9fd3f7;
    --btn-text: #ffffff;
  }
  * { box-sizing: border-box; margin: 0; padding: 0; }
  html, body { width: 852px; height: 1200px; overflow: hidden; background: var(--stage); }
  .canvas { position: relative; width: 852px; height: 1200px; }
  .screen {
    position: absolute; left: 88px; top: 0; width: 676px; height: 1200px;
    background: linear-gradient(180deg, var(--sky-top) 0%, var(--sky-mid) 45%, var(--sky-low) 100%);
    overflow: hidden; font-family: "Arimo", Arial, sans-serif;
  }
  .status-bar {
    position: absolute; left: 0; top: 0; width: 100%; height: 42px;
    background: linear-gradient(180deg, var(--status-top), var(--status-low));
    color: var(--status-ink); font-size: 26px;
    display: flex; align-items: center; padding: 0 12px;
  }
  .status-bar .carrier { display: flex; align-items: center; gap: 8px; }
  .status-bar .time { position: absolute; left: 0; right: 0; text-align: center; font-weight: 700; pointer-events: none; }
  .status-bar .indicators { margin-left: auto; display: flex; align-items: center; gap: 10px; }

  .brand { position: absolute; left: 0; top: 100px; width: 100%; text-align: center; color: var(--title); font-family: "Comfortaa", sans-serif; font-weight: 700; }
  .brand .name { line-height: 1.05; letter-spacing: 2px; font-weight: 700; }
  .brand .name .line-small { display: block; font-size: 50px; }
  .brand .name .line-big { display: block; font-size: 92px; }
  .brand .motto { margin-top: 22px; font-size: 36px; letter-spacing: 3px; }

  .play-button {
    position: absolute; left: 49px; top: 492px; width: 578px; height: 130px;
    border-radius: 65px; border: 4px solid #fff3c4;
    background: linear-gradient(180deg, var(--gold-top), var(--gold-low));
    box-shadow: 0 6px 14px rgba(0,0,0,.3);
    display: flex; align-items: center; justify-content: center; gap: 24px;
    color: var(--gold-ink); font-weight: 700; font-size: 54px; letter-spacing: 3px;
  }

  .puzzle-tiles { position: absolute; left: 49px; top: 662px; width: 578px; display: flex; gap: 20px; }
  .tile {
    flex: 1; height: 240px; border-radius: 28px; border: 3px solid var(--ring);
    background: linear-gradient(180deg, var(--tile-top), var(--tile-low));
    box-shadow: 0 6px 14px rgba(0,0,0,.3);
    display: flex; flex-direction: column; align-items: center; justify-content: center; gap: 22px;
    color: var(--btn-text); font-weight: 700; font-size: 34px; letter-spacing: 1px;
  }

  .footer-band {
    position: absolute; left: 0; top: 960px; width: 100%; height: 240px;
    background: var(--band); border-top: 2px solid var(--band-edge);
    display: flex; justify-content: space-between; padding: 30px 110px 0;
  }
  .round-button { display: flex; flex-direction: column; align-items: center; gap: 14px; color: var(--btn-text); font-weight: 700; font-size: 28px; letter-spacing: 1px; }
  .round-button .disc {
    width: 110px; height: 110px; border-radius: 50%; border: 3px solid var(--ring);
    background: linear-gradient(180deg, var(--tile-top), var(--tile-low));
    display: flex; align-items: center; justify-content: center;
    box-shadow: 0 4px 10px rgba(0,0,0,.3);
  }
</style>
</head>
<body>
<div class="canvas">
  <main class="screen">
    <header class="status-bar">
      <div class="carrier">
        <svg width="40" height="22" viewBox="0 0 40 22" aria-hidden="true">
          <rect x="0" y="14" width="5" height="8" fill="var(--signal)"/>
          <rect x="8" y="11" width="5" height="11" fill="var(--signal)"/>
          <rect x="16" y="8" width="5" height="14" fill="var(--signal)"/>
          <rect x="24" y="4" width="5" height="18" fill="var(--signal)"/>
          <rect x="32" y="0" width="5" height="22" fill="var(--signal)"/>
        </svg>
        <span>Nimbtel</span>
      </div>
      <div class="time">5:45 PM</div>
      <div class="indicators">
        <svg width="22" height="22" viewBox="0 0 22 22" aria-hidden="true"><circle cx="11" cy="11" r="9" fill="#777"/><path d="M11 5v6l4 3" stroke="#fff" stroke-width="2" fill="none"/></svg>
        <svg width="22" height="22" viewBox="0 0 22 22" aria-hidden="true"><path d="M20 2 2 10l8 2 2 8z" fill="#5a3fb0"/></svg>
        <svg width="26" height="26" viewBox="0 0 26 26" aria-hidden="true"><circle cx="13" cy="13" r="10" fill="none" stroke="#555" stroke-width="2.5"/><rect x="9" y="11" width="8" height="7" fill="#555"/><path d="M10 11V9a3 3 0 0 1 6 0v2" stroke="#555" stroke-width="2" fill="none"/></svg>
        <svg width="46" height="22" viewBox="0 0 46 22" aria-hidden="true"><rect x="1" y="1" width="40" height="20" rx="3" fill="none" stroke="#555" stroke-width="2"/><rect x="4" y="4" width="34" height="14" fill="var(--battery)"/><rect x="42" y="7" width="3" height="8" fill="#555"/></svg>
      </div>
    </header>

    <section class="brand">
      <h1 class="name">
        <span class="line-small">POLYGLYPH</span>
        <span class="line-big">GRIDWORD</span>
        <span class="line-big">RIDDLE</span>
      </h1>
      <p class="motto">gridplay rebuilt.</p>
    </section>

    <div class="play-button">
      <svg width="56" height="56" viewBox="0 0 56 56" aria-hidden="true"><circle cx="28" cy="28" r="27" fill="var(--gold-ink)"/><path d="M22 16v24l19-12z" fill="#fff"/></svg>
      <span>PLAY</span>
    </div>

    <nav class="puzzle-tiles">
      <div class="tile">
        <svg width="76" height="76" viewBox="0 0 76 76" aria-hidden="true">
          <g fill="#fff">
            <rect x="2" y="2" width="22" height="22" rx="3"/><rect x="27" y="2" width="22" height="22" rx="3"/><rect x="52" y="2" width="22" height="22" rx="3" fill="var(--gold-top)"/>
            <rect x="2" y="27" width="22" height="22" rx="3" fill="var(--gold-top)"/><rect x="27" y="27" width="22" height="22" rx="3"/><rect x="52" y="27" width="22" height="22" rx="3"/>
            <rect x="2" y="52" width="22" height="22" rx="3"/><rect x="27" y="52" width="22" height="22" rx="3" fill="var(--gold-top)"/><rect x="52" y="52" width="22" height="22" rx="3"/>
          </g>
        </svg>
        <span>MY PUZZLE</span>
      </div>
      <div class="tile">
        <svg width="80" height="76" viewBox="0 0 80 76" aria-hidden="true">
          <path d="M4 8h12l10 40h40l8-28H22" fill="none" stroke="#fff" stroke-width="6" stroke-linejoin="round" stroke-linecap="round"/>
          <circle cx="30" cy="64" r="7" fill="var(--gold-top)"/><circle cx="62" cy="64" r="7" fill="var(--gold-top)"/>
        </svg>
        <span>BUY PUZZLE</span>
      </div>
    </nav>

    <footer class="footer-band">
      <div class="round-button">
        <div class="disc">
          <svg width="48" height="48" viewBox="0 0 36 36" aria-hidden="true"><circle cx="18" cy="18" r="17" fill="#fff"/><circle cx="19" cy="10" r="3" fill="var(--tile-low)"/><path d="M15 15h5l-2 12h4" stroke="var(--tile-low)" stroke-width="4" fill="none" stroke-linejoin="round"/></svg>
        </div>
        <span>ABOUT</span>
      </div>
      <div class="round-button">
        <div class="disc">
          <svg width="50" height="50" viewBox="0 0 36 36" aria-hidden="true"><circle cx="18" cy="18" r="13" fill="none" stroke="#fff" stroke-width="6" stroke-dasharray="5 5"/><circle cx="18" cy="18" r="9" fill="none" stroke="#fff" stroke-width="5"/></svg>
        </div>
        <span>SETTING</span>
      </div>
    </footer>
  </main>
</div>
</body>
</html>
```